Business card for Industrial Automation Company.

The company is called Process and Motion Solutions. We are a systems integration company in South Africa specializing in PLC and SCADA programming, systems integration and industrial automation. Attached find logo and cover letter of the company for a feel of the general look. The website is still under development, so you will have to use your own ideas.

Please blend the colors on the business card as per the logo colors. Must be clean, professional look. Please submit a creative professional design. If a background color is used please do not use dark colored backgrounds.

Target Market(s)

Mining

Industry/Entity Type

Engineering Consultant

Contact Information for Business Card

Fanie du Plessis (NDip Electrical; BEng)
Director / Systems Engineer

Postal Address
PO Box 2836
Rooiklip
7415

Physical Address:
Bloubos Street 27
Rooiklip
7415

Tel: +22 548 6172
Cell: +27 82 395 4820
Mail: faniep@pms-za.example
Web: www.pms-za.example

Font styles to use
Sans Serif

Colors

Designer to choose colors to be used in the design.

Requirements
Must have
• Backside of the card must also contain the following:
• Services
• *Industrial Automation
• *Control System design and configuration
• *Systems Integration
• *Equipment Supply
• Industries
• *Mining
• *Factory
• *Oil and Gas
Nice to have
• Colors must blend in with colors of logo. Not too much color and no dark backgrounds.
Should not have
• dark / black background. Preferably white / light background if any.

```html
<!DOCTYPE html>
<html lang="en">
<head>
<meta charset="utf-8">
<title>Process and Motion Solutions — Business Card</title>
<link href="https://fonts.googleapis.com/css2?family=Arimo:wght@400;700&display=swap" rel="stylesheet">
<style>
  :root {
    --page: #e9e9eb;
    --card: #ffffff;
    --navy: #1f3f7a;
    --blue: #2c5aa0;
    --grey: #5f6167;
    --light-grey: #8a8c91;
    --lime: #d9df4a;
    --shadow: rgba(0, 0, 0, 0.18);
  }
  * { box-sizing: border-box; margin: 0; padding: 0; }
  html, body {
    width: 1200px; height: 844px; overflow: hidden;
    background: var(--page);
    font-family: "Arimo", Arial, sans-serif;
  }
  .sheet {
    position: relative; width: 1200px; height: 844px;
    display: flex; align-items: center; justify-content: center; gap: 48px;
  }
  .card {
    position: relative; width: 540px; height: 310px;
    background: var(--card);
    box-shadow: 0 6px 18px var(--shadow);
  }
  .brand { position: absolute; display: flex; align-items: center; gap: 10px; }
  .brand-dot { width: 14px; height: 14px; border-radius: 50%; background: var(--navy); flex: none; }
  .brand-text { display: flex; flex-direction: column; }
  .brand-name { color: var(--navy); font-weight: 700; font-size: 19px; letter-spacing: .2px; white-space: nowrap; }
  .tagline { color: var(--light-grey); font-size: 11px; letter-spacing: .8px; margin-top: 3px; white-space: nowrap; }

  /* front */
  .front .brand { top: 50px; left: 150px; }
  .person { position: absolute; left: 30px; top: 168px; }
  .person-name { color: var(--navy); font-weight: 700; font-size: 17px; letter-spacing: .3px; white-space: nowrap; }
  .person-name .quals { font-weight: 400; font-size: 14px; color: var(--blue); }
  .role { color: var(--grey); font-size: 13px; margin-top: 2px; }
  .contacts { list-style: none; margin-top: 14px; }
  .contacts li { display: flex; align-items: center; gap: 7px; color: var(--grey); font-size: 13px; line-height: 18px; white-space: nowrap; }
  .contacts svg { width: 12px; height: 12px; fill: var(--navy); flex: none; }
  .address { position: absolute; padding-left: 14px; border-left: 1.5px solid var(--lime); }
  .address.postal { left: 250px; top: 200px; }
  .address.physical { left: 385px; top: 150px; }
  .address h3 { color: var(--blue); font-weight: 400; font-size: 14px; margin-bottom: 4px; white-space: nowrap; }
  .address p { color: var(--grey); font-size: 13.5px; line-height: 18px; white-space: nowrap; }

  /* back */
  .back .brand { top: 52px; left: 70px; }
  .industries { position: absolute; left: 410px; top: 48px; padding-left: 14px; border-left: 1.5px solid var(--lime); height: 92px; }
  .services { position: absolute; left: 40px; top: 190px; }
  .section-title { color: var(--navy); font-weight: 700; font-size: 12.5px; letter-spacing: .3px; margin-bottom: 8px; }
  .bullets { list-style: none; }
  .bullets li { display: flex; align-items: center; gap: 6px; color: var(--grey); font-size: 12px; line-height: 16px; white-space: nowrap; }
  .bullets li::before { content: ""; width: 6px; height: 6px; border-radius: 50%; background: var(--navy); flex: none; }
  .services .bullets { display: flex; flex-wrap: wrap; width: 330px; column-gap: 10px; }
  .services .bullets li { font-size: 13px; line-height: 18px; }
  .services .bullets li.wide { width: 100%; }
  .services .bullets li::before { width: 8px; height: 8px; background: var(--blue); }
</style>
</head>
<body>
<main class="sheet">
  <section class="card front" aria-label="Card front">
    <div class="brand">
      <span class="brand-dot"></span>
      <div class="brand-text">
        <span class="brand-name">Process and Motion Solutions</span>
        <span class="tagline">Engineering dependable automation!</span>
      </div>
    </div>

    <div class="person">
      <h1 class="person-name">FANIE DU PLESSIS <span class="quals">(NDip Electrical; BEng)</span></h1>
      <p class="role">Director / Systems Engineer</p>
      <ul class="contacts">
        <li><svg viewBox="0 0 12 12"><path d="M1 4c0-2 1-3 5-3s5 1 5 3H8.5V3h-5v1zM2 5h8l1 6H1z"/></svg>+22 548 6172</li>
        <li><svg viewBox="0 0 12 12"><path d="M3 0h6a1 1 0 0 1 1 1v10a1 1 0 0 1-1 1H3a1 1 0 0 1-1-1V1a1 1 0 0 1 1-1zm0 2v7h6V2z"/></svg>+27 82 395 4820</li>
        <li><svg viewBox="0 0 12 12"><path d="M0 2h12v8H0zm1 1v.5l5 3 5-3V3z"/></svg>faniep@pms-za.example</li>
        <li><svg viewBox="0 0 12 12"><circle cx="6" cy="6" r="5.5"/></svg>www.pms-za.example</li>
      </ul>
    </div>

    <div class="address postal">
      <h3>Postal Address</h3>
      <p>PO Box 2836<br>Rooiklip<br>7415</p>
    </div>
    <div class="address physical">
      <h3>Physical Address</h3>
      <p>Bloubos Street 27<br>Rooiklip<br>7415</p>
    </div>
  </section>

  <section class="card back" aria-label="Card back">
    <div class="brand">
      <span class="brand-dot"></span>
      <div class="brand-text">
        <span class="brand-name">Process and Motion Solutions</span>
        <span class="tagline">Engineering dependable automation!</span>
      </div>
    </div>

    <div class="industries">
      <h2 class="section-title">INDUSTRIES</h2>
      <ul class="bullets">
        <li>Mining</li>
        <li>Factory</li>
        <li>Oil and Gas</li>
      </ul>
    </div>

    <div class="services">
      <h2 class="section-title">SERVICES</h2>
      <ul class="bullets">
        <li class="wide">Industrial Automation</li>
        <li class="wide">Control System design and configuration</li>
        <li>Systems Integration</li>
        <li>Equipment Supply</li>
      </ul>
    </div>
  </section>
</main>
</body>
</html>
```